Brindle and Fern LLC | Land Clearing, Landscaping & Dump Trailer Services

Project Description: Brindle and Fern LLC Website Design
The website will be published using squarespace
Objective:
Design a visually compelling and conversion-driven website for Brindle and Fern LLC, a land solutions business based in Pickens County, Georgia. The site will highlight the company’s professionalism, locally rooted service, and commitment to quality in land clearing, grading, and dump trailer services.
Pages & Features to Include:
1. Landing Page (Homepage)
- Clear tagline: Sculpting Land with Precision and Power
- Call-to-Action (CTA) buttons: “Get a Free Quote” and “View Services”
- Service highlights with icons or photos (e.g., grading, mulching, hauling)
- Customer testimonials
- Embedded contact form
- Google Maps integration showing service area
2. Services + Pricing Page
- Organized list of services under 3 categories:
- **Land Clearing & Grading**
- Forestry Mulching
- Gravel Driveway Repair
- Minimum Job Fee:
- Dump Trailer Services
- Trailer Rental (Daily):
- Junk Removal (Full Load)
- Material Delivery: $ + mileage
- Specialty Jobs
- Stump removal, light demolition
- Each service section includes short descriptions and photos
- Optional quote form at the bottom with “Request a Quote” CTA
Design Style:
- Clean, professional design using clean tones
- Fonts that balance industrial strength and local charm
- Mobile-optimized with fast loading speeds and easy navigation
- SEO-optimized for terms like *land clearing Pickens County*, *grading services North Georgia*, and *dump trailer rental Jasper GA*, etc...

```html
<!DOCTYPE html>
<html lang="en">
<head>
<meta charset="utf-8">
<title>Brindle and Fern LLC | Land Clearing, Grading &amp; Dump Trailer Services</title>
<link rel="stylesheet" href="https://fonts.googleapis.com/css2?family=Michroma&family=Poppins:ital,wght@0,400;0,500;0,600;1,400&display=swap">
<style>
:root{
  --green:#0b7a3e;
  --green-dark:#06682f;
  --green-form:rgba(11,122,62,.9);
  --ink:#1c1c1c;
  --body:#333;
  --white:#fff;
  --panel:#f4f4f4;
  --map:#ececec;
}
*{box-sizing:border-box;margin:0;padding:0}
html,body{width:1200px;height:3949px;overflow:hidden}
body{position:relative;font-family:"Poppins",sans-serif;color:var(--body);background:var(--white)}
.abs{position:absolute}
.display{font-family:"Michroma",sans-serif;font-weight:400;text-transform:uppercase;letter-spacing:-.5px}
.btn{position:absolute;display:flex;align-items:center;justify-content:center;background:var(--green);color:var(--white);font-weight:600;text-transform:uppercase;font-size:15px;text-decoration:none}

/* hero */
.hero{left:0;top:0;width:1200px;height:680px;background:linear-gradient(180deg,#4d5148 0%,#6f6d5e 35%,#8a7a5e 65%,#6e5a40 100%)}
.hero::after{content:"";position:absolute;inset:0;background:rgba(0,0,0,.28)}
.hero-inner{position:absolute;inset:0;z-index:1}
.logo{left:126px;top:48px;font-size:30px;color:var(--white)}
.nav a{position:absolute;top:57px;font-size:16px;font-weight:500;color:var(--white);text-decoration:none}
.nav a.active{border-bottom:2px solid var(--white);padding-bottom:3px}
.hero h1{left:0;width:1200px;top:262px;text-align:center;color:var(--white);font-size:42px;line-height:52px}
.hero .btn{border:2px solid var(--white);top:386px;height:57px;font-size:16px}

/* welcome */
.welcome-panel{left:0;top:680px;width:588px;height:495px;background:var(--panel)}
.welcome-photo{left:588px;top:680px;width:612px;height:495px;background:linear-gradient(180deg,#9fb3c4 0%,#c8cdcf 30%,#7b7360 60%,#5a4a38 100%)}
.welcome h2{left:127px;top:792px;font-size:37px;line-height:43px;color:var(--ink)}
.welcome p{left:127px;top:900px;width:385px;font-size:16px;line-height:25px}

/* services */
.section-title{left:0;width:1200px;text-align:center;color:var(--ink);font-size:36px}
.card-photo{top:1375px;width:290px;height:308px}
.card h3{top:1710px;font-size:23px;color:var(--ink)}
.card p{top:1753px;width:290px;font-size:15.5px;line-height:25px}
.card .btn{top:1877px;width:135px;height:49px}
.arrow{top:1485px;width:40px;height:50px}

/* testimonials */
.testimonials{left:0;top:2077px;width:1200px;height:479px;background:linear-gradient(135deg,#0e8444 0%,var(--green) 50%,var(--green-dark) 100%)}
.testimonials .section-title{color:var(--white);top:2156px}
.avatar{left:232px;top:2260px;width:188px;height:188px;border-radius:50%;background:radial-gradient(circle at 40% 40%,#e5b56a,#8e6a3a 70%,#5b4a2a)}
.t-name{left:448px;top:2264px;font-size:19px;font-weight:600;color:var(--white);text-transform:uppercase}
.t-quote{left:448px;top:2300px;width:515px;font-size:15.5px;line-height:25px;font-style:italic;color:var(--white)}
.stars{left:448px;top:2412px}
.quote-mark{left:985px;top:2330px;font-family:"Poppins",sans-serif;font-size:260px;line-height:1;font-weight:600;color:rgba(255,255,255,.18)}

/* contact */
.contact .section-title{top:2640px;font-size:38px}
.contact-lead{left:0;width:1200px;top:2700px;text-align:center;font-size:15.5px;line-height:25px}
.contact-photo{left:0;top:2774px;width:1200px;height:495px;background:linear-gradient(180deg,#c9cdc4 0%,#9a9c88 35%,#7a5e40 70%,#5e4530 100%)}
.form-box{left:248px;top:2774px;width:705px;height:409px;background:var(--green-form)}
.field{position:absolute;border:1px solid rgba(255,255,255,.75);color:var(--white);font-size:15px;padding:10px 14px}
.submit{left:520px;top:3094px;width:160px;height:48px;background:var(--white);color:var(--green);font-weight:600;font-size:16px;display:flex;align-items:center;justify-content:center;text-transform:uppercase}

/* map */
.map{left:0;top:3269px;width:1200px;height:440px;background:linear-gradient(135deg,#f1f1f1,#e4e4e4)}
.map-card{left:380px;top:3410px;width:299px;height:173px;background:var(--white);box-shadow:0 4px 18px rgba(0,0,0,.12)}
.map-row{position:absolute;left:27px;display:flex;gap:12px;font-size:16px;line-height:21px;color:var(--ink)}
.map-icon{width:34px;height:34px;background:var(--green);flex:none;display:flex;align-items:center;justify-content:center}

/* footer */
.footer-logo{left:0;width:1200px;top:3768px;text-align:center;color:var(--green);font-size:35px}
.copyright{left:0;width:1200px;top:3822px;text-align:center;font-size:15px;color:var(--ink)}
.social{top:3862px;width:30px;height:30px;border-radius:50%;background:var(--green)}
</style>
</head>
<body>

<section class="hero abs" role="img" aria-label="Yellow excavator clearing a wooded lot">
  <div class="hero-inner">
    <div class="logo abs display">Brindle &amp; Fern LLC</div>
    <nav class="nav">
      <a class="active" href="#" style="left:730px">Home</a>
      <a href="#" style="left:820px">Services &amp; Pricing</a>
      <a href="#" style="left:1007px">Contact</a>
    </nav>
    <h1 class="abs display">Sculpting Land with<br>Precision and Power</h1>
    <a class="btn" href="#" style="left:391px;width:202px">Get a Free Quote</a>
    <a class="btn" href="#" style="left:607px;width:202px">View Services</a>
  </div>
</section>

<section class="welcome">
  <div class="welcome-panel abs"></div>
  <div class="welcome-photo abs" role="img" aria-label="Red wheel loader moving soil on a roadside site"></div>
  <h2 class="abs display">Welcome to<br>Brindle and Fern</h2>
  <p class="abs">Lorem ipsum dolor sit amet, consectetur dipisc ing elit, sed do eiusmod tempor incididunt ut labore et dolore magna aliqua. Quis ips lorum suspendisse ultrices gravida. Risus commodo viverra maecenas accumsan lacus vel faci lisisices gravida. Risus commodo viverra maecenas accumsan lacus.</p>
</section>

<section class="services">
  <h2 class="section-title abs display" style="top:1284px">Our Services</h2>
  <svg class="arrow abs" style="left:60px" viewBox="0 0 40 50"><path d="M28 5 L10 25 L28 45" fill="none" stroke="#111" stroke-width="6"/></svg>
  <svg class="arrow abs" style="left:1100px" viewBox="0 0 40 50"><path d="M12 5 L30 25 L12 45" fill="none" stroke="#111" stroke-width="6"/></svg>

  <div class="card">
    <div class="card-photo abs" style="left:127px;background:linear-gradient(180deg,#6f8a5a,#8a7a5a 55%,#5d4a35)" role="img" aria-label="Yellow loader bucket grading soil in a park"></div>
    <h3 class="abs display" style="left:127px">Grading</h3>
    <p class="abs" style="left:127px">Lorem ipsum dolor sit amet, conse ctetur dipiscing elit, sed do eiusmod tempor incididunt ut labore etolore magna aliqua.</p>
    <a class="btn" href="#" style="left:128px">Read More</a>
  </div>
  <div class="card">
    <div class="card-photo abs" style="left:455px;background:linear-gradient(180deg,#7c6a58,#6b5a48 50%,#4f4034)" role="img" aria-label="Gloved hands spreading mulch in a garden bed"></div>
    <h3 class="abs display" style="left:455px">Mulching</h3>
    <p class="abs" style="left:455px">Lorem ipsum dolor sit amet, conse ctetur dipiscing elit, sed do eiusmod tempor incididunt ut labore etolore magna aliqua.</p>
    <a class="btn" href="#" style="left:456px">Read More</a>
  </div>
  <div class="card">
    <div class="card-photo abs" style="left:780px;background:linear-gradient(180deg,#4d6a3a,#6a7a3a 50%,#6a5a3a)" role="img" aria-label="Forestry machine hauling logs in a pine forest"></div>
    <h3 class="abs display" style="left:780px">Hauling</h3>
    <p class="abs" style="left:780px">Lorem ipsum dolor sit amet, conse ctetur dipiscing elit, sed do eiusmod tempor incididunt ut labore etolore magna aliqua.</p>
    <a class="btn" href="#" style="left:781px">Read More</a>
  </div>
</section>

<section class="testimonials abs"></section>
<h2 class="section-title abs display" style="top:2156px;color:#fff">Customer Testimonials</h2>
<div class="avatar abs" role="img" aria-label="Customer portrait in warm sunlight"></div>
<div class="t-name abs">Marla Quinlen Dove</div>
<p class="t-quote abs">Lorem ipsum dolor sit amet, consectetur adipiscing elit, sed do eiusmod tempor incididunt ut labore et dolore magna aliqua uis ipsum suspendisse ultrices gravida. Risus commodo viverra maecenas accumsan lacus vel facilisis.</p>
<svg class="stars abs" width="86" height="16" viewBox="0 0 86 16" aria-label="Five stars">
  <g fill="#fff">
    <path id="st" d="M7 1l1.8 4.2 4.5.4-3.4 3 1 4.4L7 10.7 3.1 13l1-4.4-3.4-3 4.5-.4z"/>
    <use href="#st" x="17"/><use href="#st" x="34"/><use href="#st" x="51"/><use href="#st" x="68"/>
  </g>
</svg>
<div class="quote-mark abs" aria-hidden="true">&#8221;</div>

<section class="contact">
  <h2 class="section-title abs display">Contact Us</h2>
  <p class="contact-lead abs">Lorem ipsum dolor sit amet, conse ctetur dipiscing elit, sed dusm<br>od tempor incididunt ut labore etolore magna aliqua.</p>
  <div class="contact-photo abs" role="img" aria-label="Cleared lot of bare earth with trees and houses behind"></div>
  <form class="form-box abs">
    <div class="field" style="left:72px;top:51px;width:273px;height:42px">Name:</div>
    <div class="field" style="left:357px;top:51px;width:273px;height:42px">Email:</div>
    <div class="field" style="left:72px;top:121px;width:273px;height:43px">Phone:</div>
    <div class="field" style="left:357px;top:121px;width:273px;height:43px">Subject:</div>
    <div class="field" style="left:72px;top:198px;width:558px;height:89px">Message:</div>
  </form>
  <div class="submit abs">Submit Now</div>
</section>

<section class="map abs" role="img" aria-label="Map of the service area"></section>
<div class="map-card abs">
  <div class="map-row" style="top:36px">
    <span class="map-icon"><svg width="18" height="18" viewBox="0 0 24 24" fill="none" stroke="#fff" stroke-width="2"><path d="M12 22s7-7 7-12a7 7 0 0 0-14 0c0 5 7 12 7 12z"/><circle cx="12" cy="10" r="2.5"/></svg></span>
    <span>Brindle and Fern LLC<br>Jasper, Oak Street 12, GA 301</span>
  </div>
  <div class="map-row" style="top:96px">
    <span class="map-icon"><svg width="18" height="18" viewBox="0 0 24 24" fill="none" stroke="#fff" stroke-width="2"><path d="M5 3h4l2 5-2.5 1.5a11 11 0 0 0 6 6L16 13l5 2v4a2 2 0 0 1-2 2A17 17 0 0 1 3 5a2 2 0 0 1 2-2z"/></svg></span>
    <span>Phone:<br>555 0142 218</span>
  </div>
</div>

<footer>
  <div class="footer-logo abs display">Brindle &amp; Fern LLC</div>
  <p class="copyright abs">Copyright © 2025 Brindle and Fern LLC. All Rights Reserved.</p>
  <span class="social abs" style="left:524px" aria-label="Social link"></span>
  <span class="social abs" style="left:564px" aria-label="Social link"></span>
  <span class="social abs" style="left:604px" aria-label="Social link"></span>
  <span class="social abs" style="left:644px" aria-label="Social link"></span>
</footer>

</body>
</html>
```